Business Card for Marriage Commissioner

I am a marriage commissioner in the province of Alberta, meaning that I perform civil unions here. I have been trying to think of a unique design for my business card, something a bit different. A lot of "unique" designs seem to incorporate unique cuts or "some assembly required" or printed on plastic or meat. I would like my design to be a full colour card that is a typical business card size.

The information on the card should have:
Lou Varnik
my occupation: Marriage Commissioner
my website: www.louvarnik.ca
my e-mail: lou@louvarnik.ca
my phone: 780-418-2964

I originally submitted a design to the printer that had a screen capture of a findly search window, with my name and occupation in the text box. And underneath that, my phone number. Nothing else. They indicated they could not print this because it was a copyright violation.

One option on the design is I am a retired chemist-so a chemistry themed card would also be of interest, as long as it isn't a "Rusted Tide" theme, as I have that on my other business cards already...

I would prefer a single sided card, but I am open to a double sided card if it is clever!

I would also prefer not to have pictures of male and female couples as in my position I will also marry same sex couples. Same thing for male/female symbols. Someone has submitted two graduated cylinders in love, which is very clever, and gets around this male/female type.

Thanks for your help and interest.

Target Market(s)

Young couples.

Industry/Entity Type

Plastic

Requirements
Nice to have
• chemistry ideas!
Should not have
• Male/female pictures, male/female symbols.
No QR codes.
No transparent designs, will go on paper stock.

```html
<!DOCTYPE html>
<html lang="en">
<head>
<meta charset="utf-8">
<title>Lou Varnik – Marriage Commissioner Business Card</title>
<link rel="stylesheet" href="https://fonts.googleapis.com/css2?family=PT+Serif:wght@400;700&display=swap">
<style>
  :root {
    --page-bg: #d9d9d9;
    --card-white: #ffffff;
    --band-blue: #3f66b8;
    --band-blue-dark: #2f53a3;
    --band-orange: #f0902a;
    --band-orange-deep: #e55a24;
    --ink: #1f1f1f;
    --accent-red: #d8262c;
  }
  * { margin: 0; padding: 0; box-sizing: border-box; }
  html, body {
    width: 1200px;
    height: 810px;
    overflow: hidden;
    background: var(--page-bg);
  }
  .canvas {
    position: relative;
    width: 1200px;
    height: 810px;
    display: flex;
    align-items: center;
    justify-content: center;
  }
  .business-card {
    position: relative;
    width: 1050px;
    height: 600px;
    background: var(--card-white);
    box-shadow: 0 10px 30px rgba(0,0,0,0.18);
    font-family: "PT Serif", Georgia, serif;
    color: var(--ink);
    overflow: hidden;
  }
  .card-bands {
    position: absolute;
    inset: 0;
    width: 100%;
    height: 100%;
  }
  .identity {
    position: absolute;
    left: 170px;
    top: 175px;
    width: 720px;
  }
  .identity__name {
    font-size: 118px;
    font-weight: 400;
    line-height: 1;
    letter-spacing: 1px;
  }
  .identity__rule {
    height: 2px;
    background: var(--accent-red);
    margin-top: 10px;
    width: 100%;
  }
  .identity__role {
    font-size: 30px;
    letter-spacing: 4px;
    text-transform: uppercase;
    margin-top: 8px;
    padding-left: 70px;
  }
  .contact-list {
    position: absolute;
    left: 220px;
    top: 400px;
    width: 700px;
    list-style: none;
    display: flex;
    flex-wrap: wrap;
    column-gap: 60px;
    row-gap: 10px;
    font-size: 30px;
    letter-spacing: 1px;
  }
  .contact-list__item {
    display: flex;
    align-items: center;
    gap: 12px;
  }
  .contact-list__item--web {
    width: 100%;
    padding-left: 170px;
    font-weight: 700;
  }
  .contact-icon {
    width: 22px;
    height: 22px;
    flex: none;
  }
</style>
</head>
<body>
<main class="canvas">
  <article class="business-card">
    <svg class="card-bands" viewBox="0 0 1050 600" preserveAspectRatio="none" aria-hidden="true">
      <defs>
        <linearGradient id="orange-band" x1="0" y1="0" x2="0" y2="1">
          <stop offset="0" stop-color="var(--band-orange)" />
          <stop offset="1" stop-color="var(--band-orange-deep)" />
        </linearGradient>
        <linearGradient id="blue-band" x1="0" y1="0" x2="1" y2="0">
          <stop offset="0" stop-color="var(--band-blue-dark)" />
          <stop offset="1" stop-color="var(--band-blue)" />
        </linearGradient>
      </defs>
      <polygon fill="url(#blue-band)" points="0,0 1050,0 1050,110 960,28 300,28 0,140" />
      <polygon fill="url(#orange-band)" points="0,470 190,545 870,545 1050,470 1050,600 0,600" />
    </svg>

    <header class="identity">
      <h1 class="identity__name">Lou Varnik</h1>
      <p class="identity__role">Marriage Commissioner</p>
      <div class="identity__rule"></div>
    </header>

    <ul class="contact-list">
      <li class="contact-list__item contact-list__item--phone">
        <svg class="contact-icon" viewBox="0 0 22 22" aria-hidden="true">
          <rect x="5" y="2" width="12" height="18" rx="2" fill="none" stroke="var(--accent-red)" stroke-width="2.2"/>
          <line x1="9" y1="16.5" x2="13" y2="16.5" stroke="var(--accent-red)" stroke-width="1.8"/>
        </svg>
        <span>780-418-2964</span>
      </li>
      <li class="contact-list__item contact-list__item--email">
        <svg class="contact-icon" viewBox="0 0 22 22" aria-hidden="true">
          <rect x="2" y="5" width="18" height="12" fill="var(--accent-red)"/>
          <polyline points="2,5 11,12 20,5" fill="none" stroke="#fff" stroke-width="1.6"/>
        </svg>
        <span>lou@louvarnik.ca</span>
      </li>
      <li class="contact-list__item contact-list__item--web">
        <svg class="contact-icon" viewBox="0 0 22 22" aria-hidden="true">
          <circle cx="11" cy="11" r="9.5" fill="var(--accent-red)"/>
          <ellipse cx="11" cy="11" rx="4" ry="9.5" fill="none" stroke="#fff" stroke-width="1.4"/>
          <line x1="1.5" y1="11" x2="20.5" y2="11" stroke="#fff" stroke-width="1.4"/>
        </svg>
        <span>www.louvarnik.ca</span>
      </li>
    </ul>
  </article>
</main>
</body>
</html>
```